Wim pod OBR is the name of my childrens book for middle school kids. I'm looking to get a book cover

I'm looking to get an interesting book cover for the book I'm working on called Wim OBR. It is a book about a middle school kid and his family and friends.It is first one. in a series of books.The book size is 8 1/2 x 5 1/2 .The book is written like a diary much like Scraps of a gloomy sprout or Fizzle Capers. It should have the look and feel of a diary or journal. For this first book I wanted to use yellow or gold color for the cover. But if you have a better Idea go for it! I already have a logo which I'll upload for your review which has to go on the cover. I'm looking for unusual and different ideas so please be as creative as you want to be. Thanks

Target Market(s)

Middle school kids ages 9 to 12

Industry/Entity Type

School

Font styles to use
Serif

Colors
ffcf3e
ffc214
ec1f27
f04a51
0456a4
3176b5
85acd3
9ccb3b
acd136

Requirements
Must have
• My Logo ( which is the title of the book. Wim Pod OBR) I Uploaded it. The Subtitle: Chasing clouds and Counting Pebbles. Main character on the cover. I uploaded two different versions of main characters. Please use either one. Please redraw if necessary.
Nice to have
• Maybe look like a Diary or journal with lock and key or combination lock or different type of diary. But doesn't have to look like that.
Should not have
• The Flag, Stars and stripes,

```html
<!DOCTYPE html>
<html lang="en">
<head>
<meta charset="utf-8">
<title>Wim Pod OBR – Book Cover Wrap</title>
<link rel="stylesheet" href="https://fonts.googleapis.com/css2?family=Cinzel:wght@400;700&family=Amatic+SC:wght@700&family=EB+Garamond:wght@400&display=swap">
<style>
  :root {
    --page-bg: #f2f2f2;
    --sky: #d4ebf7;
    --cloud: #ffffff;
    --ground: #9e9a2c;
    --spine: #f0b41c;
    --spine-edge: #d99b10;
    --title-red: #d3372c;
    --ink: #161616;
    --body-ink: #222222;
    --figure-warm: #c7473a;
    --figure-gold: #f2bf2c;
    --figure-skin: #f7c98e;
  }
  * { margin: 0; padding: 0; box-sizing: border-box; }
  html, body { width: 1200px; height: 800px; overflow: hidden; background: var(--page-bg); }
  .wrap {
    position: absolute; left: 126px; top: 50px;
    width: 948px; height: 700px; display: flex;
    box-shadow: 0 10px 30px rgba(0,0,0,0.12);
  }
  .cover {
    position: relative; width: 460px; height: 700px; overflow: hidden;
    background: linear-gradient(var(--sky) 0%, var(--sky) 80%, var(--ground) 80%);
  }
  .cover--back { background: linear-gradient(#ffffff 0%, var(--sky) 40%, var(--sky) 78%, var(--ground) 78%); }
  .clouds { position: absolute; left: 0; top: 0; width: 460px; height: 700px; }
  .ground-band {
    position: absolute; left: 0; bottom: 0; width: 100%; height: 20%;
    background: var(--ground);
  }
  .cover--back .ground-band { height: 22%; }

  .logo-title {
    position: absolute; font-family: "Cinzel", serif; font-weight: 700;
    color: var(--title-red); line-height: 1; text-align: center; white-space: nowrap;
  }
  .cover--front .logo-title { left: 20px; top: 34px; width: 420px; font-size: 66px; }
  .logo-title .logo-line-2 { display: block; font-size: 0.62em; }
  .subtitle {
    position: absolute; left: 10px; top: 212px; width: 440px; text-align: center;
    font-family: "Amatic SC", sans-serif; font-weight: 700; white-space: nowrap;
    font-size: 31px; letter-spacing: 0.5px; color: var(--ink);
  }
  .hero-figure {
    position: absolute; left: 70px; top: 270px; width: 300px; height: 430px;
    border-radius: 140px 140px 0 0;
    background: linear-gradient(160deg, var(--figure-skin) 0%, var(--figure-warm) 45%, var(--figure-gold) 75%, var(--figure-warm) 100%);
  }
  .author-name {
    position: absolute; left: 0; top: 618px; width: 100%; text-align: center;
    font-family: "Cinzel", serif; font-weight: 400; font-size: 48px; color: var(--ink);
    white-space: nowrap;
  }

  .spine {
    position: relative; width: 28px; height: 700px; flex: none;
    background: linear-gradient(90deg, var(--spine-edge), var(--spine) 40%, var(--spine));
    display: flex; flex-direction: column; align-items: center; padding: 24px 0;
    overflow: hidden;
  }
  .spine span { writing-mode: vertical-rl; white-space: nowrap; }
  .spine-subtitle { font-family: "Amatic SC", sans-serif; font-weight: 700; font-size: 13px; color: var(--ink); letter-spacing: 1px; }
  .spine-logo { margin-top: 60px; font-family: "Cinzel", serif; font-weight: 700; font-size: 14px; color: var(--title-red); }
  .spine-author { margin-top: 60px; font-family: "Cinzel", serif; font-size: 15px; color: var(--ink); letter-spacing: 1px; }

  .blurb {
    position: absolute; left: 24px; top: 40px; width: 410px;
    font-family: "EB Garamond", serif; font-size: 12.6px; line-height: 1.36;
    color: var(--body-ink); text-align: justify; hyphens: auto;
  }
  .blurb p + p { margin-top: 16px; }
  .cover--back .logo-title { right: 30px; top: 440px; font-size: 44px; width: 220px; }
</style>
</head>
<body>
<main class="wrap">
  <section class="cover cover--back" aria-label="Back cover">
    <div class="ground-band"></div>
    <div class="blurb">
      <p>Lorem ipsum dolor sit amet, consectetur adipiscing elit. Aliquam dictum, tortor et sagittis ullamcorper, quam felis egestas risus, ut tristique orci purus ac nunc. Donec venenatis libero at sodales condimentum. Nulla sagittis leo quis gravida consequat. Curabitur placerat scelerisque arcu. Donec pretium aliquet orci fermentum malesuada. Sed luctus sodales efficitur. Ut sed interdum libero. Donec elementum placerat dolor eget elementum. Quisque eget velit urna. Phasellus bibendum, odio a sodales sollicitudin, velit elit porta dui, eu convallis nibh quam a odio. Sed fermentum aliquam mi, id ullamcorper augue. Nullam sapien justo, mattis sed aliquet vitae, condimentum in nulla. Curabitur sapien nisi, cursus nec maximus quis, semper non purus. Quisque a nisi porttitor metus sollicitudin lacinia. Aliquam erat volutpat.</p>
      <p>Ut volutpat arcu nec ex imperdiet viverra. Nam non maximus turpis. Vestibulum ut rutrum elit, et fringilla mauris. Suspendisse suscipit tincidunt neque in mollis. Integer sed tempor justo. Proin tempus eget tellus sed facilisis. Etiam et aliquet massa, nec bibendum dui. Aenean et dui libero. Integer leo felis, venenatis at odio in, laoreet lobortis sapien. In gravida sapien ac turpis placerat, id mattis sem pharetra. Phasellus porttitor scelerisque dictum. Vivamus malesuada, quam sit amet scelerisque sollicitudin, mi dolor pellentesque arcu, sed egestas enim massa in quam. In pharetra rutrum magna a tincidunt. Suspendisse non sapien odio. Fusce sed diam placerat, sagittis eros non, posuere ligula. Suspendisse et mattis odio.</p>
    </div>
    <div class="logo-title">Wim Pod<span class="logo-line-2">OBR</span></div>
  </section>

  <aside class="spine" aria-label="Spine">
    <span class="spine-subtitle">Chasing clouds and Counting Pebbles</span>
    <span class="spine-logo">Wim Pod OBR</span>
    <span class="spine-author">AUTHOR NAME</span>
  </aside>

  <section class="cover cover--front" aria-label="Front cover">
    <svg class="clouds" viewBox="0 0 460 700" aria-hidden="true">
      <g fill="var(--cloud)">
        <rect x="0" y="240" width="460" height="240"/>
        <ellipse cx="60" cy="225" rx="80" ry="45"/>
        <ellipse cx="190" cy="195" rx="110" ry="55"/>
        <ellipse cx="340" cy="205" rx="100" ry="50"/>
        <ellipse cx="440" cy="230" rx="60" ry="40"/>
      </g>
    </svg>
    <div class="ground-band"></div>
    <div class="logo-title">Wim Pod<span class="logo-line-2">OBR</span></div>
    <div class="subtitle">Chasing clouds and Counting Pebbles</div>
    <div class="hero-figure" role="img" aria-label="Illustration of a middle school boy in a red shirt reading his yellow journal, Theo's Journal, sitting on a grassy hill"></div>
    <div class="author-name">AUTHOR NAME</div>
  </section>
</main>
</body>
</html>
```